Pelbrook Business Cards

Create new business cards with the details below.

Aaron Velst
Director

MB: +61 412 563 904
PH: 1300 417 639
Email: aaron.velst@pelbrook.com.au
Address: 27C Marlow Parade, Ashvale VIC 3094 Australia
Website: www.pelbrook.com.au

Target Market(s)

Other business

Industry/Entity Type

Business

Requirements
Must have
• must be clean looking

```html
<!DOCTYPE html>
<html lang="en">
<head>
<meta charset="utf-8">
<title>Pelbrook Business Cards</title>
<link rel="stylesheet" href="https://fonts.googleapis.com/css2?family=Montserrat:wght@600;700&family=Inter:wght@300;400;500&display=swap">
<style>
  :root {
    --page: #e9e8e6;
    --wood-light: #cfcbc6;
    --wood-mid: #a9a39d;
    --wood-dark: #8a847e;
    --panel: #333436;
    --green: #8cc63f;
    --ink-light: #e6e6e6;
    --ink-muted: #b9b9b9;
    --logo-ink: #3a3b3d;
  }
  * { margin: 0; padding: 0; box-sizing: border-box; }
  html, body { width: 1200px; height: 800px; overflow: hidden; }
  body {
    background: var(--page);
    font-family: "Inter", Arial, sans-serif;
    position: relative;
  }
  .card {
    position: absolute;
    top: 241px;
    width: 520px;
    height: 318px;
    border-radius: 4px;
    overflow: hidden;
    box-shadow: 0 6px 18px rgba(0,0,0,0.18);
  }
  .card--front { left: 60px; }
  .card--back { left: 620px; }
  .wood-texture {
    position: absolute; inset: 0;
    background: linear-gradient(175deg, var(--wood-light) 0%, var(--wood-mid) 45%, var(--wood-light) 70%, var(--wood-dark) 100%);
  }
  .brand {
    position: absolute;
    left: 0; right: 0; top: 50%;
    transform: translateY(-50%);
    display: flex; align-items: center; justify-content: center; gap: 18px;
  }
  .brand__mark {
    width: 46px; height: 46px;
    background: var(--green);
  }
  .brand__name {
    font-family: "Montserrat", Arial, sans-serif;
    font-weight: 700;
    font-size: 62px;
    letter-spacing: 1px;
    text-transform: uppercase;
    color: var(--logo-ink);
  }
  .info-panel {
    position: absolute;
    top: 0; bottom: 0;
    left: 74px; width: 358px;
    background: var(--panel);
    border-left: 12px solid var(--green);
    border-right: 12px solid var(--green);
    color: var(--ink-light);
  }
  .person { position: absolute; left: 34px; top: 56px; }
  .person__name { font-weight: 300; font-size: 22px; letter-spacing: 0.2px; }
  .person__title { font-weight: 500; font-size: 15px; color: var(--green); margin-top: 2px; }
  .contact { position: absolute; left: 34px; top: 198px; font-size: 13px; }
  .contact__email { font-weight: 500; margin-bottom: 4px; }
  .contact__phones { display: flex; align-items: center; gap: 10px; }
  .phone-icon { width: 18px; height: 32px; }
  .contact__line { font-weight: 500; line-height: 17px; }
  .contact__label { color: var(--green); font-weight: 300; margin-right: 4px; }
  .contact__address {
    position: absolute; left: 20px; bottom: 22px;
    font-size: 11.5px; font-weight: 300; color: var(--ink-muted);
    white-space: nowrap;
  }
</style>
</head>
<body>
  <section class="card card--front">
    <div class="wood-texture" role="img" aria-label="Weathered grey timber plank texture"></div>
    <div class="brand">
      <span class="brand__mark"></span>
      <span class="brand__name">Pelbrook</span>
    </div>
  </section>

  <section class="card card--back">
    <div class="wood-texture" role="img" aria-label="Weathered grey timber plank texture"></div>
    <div class="info-panel">
      <div class="person">
        <p class="person__name">Aaron Velst</p>
        <p class="person__title">Director</p>
      </div>
      <div class="contact">
        <p class="contact__email">aaron.velst@pelbrook.com.au</p>
        <div class="contact__phones">
          <svg class="phone-icon" viewBox="0 0 18 32" aria-hidden="true">
            <rect x="1" y="1" width="16" height="30" rx="3" fill="none" stroke="#bdbdbd" stroke-width="1.5"/>
            <line x1="1.5" y1="5" x2="16.5" y2="5" stroke="#bdbdbd" stroke-width="1"/>
            <line x1="1.5" y1="25" x2="16.5" y2="25" stroke="#bdbdbd" stroke-width="1"/>
          </svg>
          <div>
            <p class="contact__line"><span class="contact__label">MB:</span>+61 412 563 904</p>
            <p class="contact__line"><span class="contact__label">PH:</span>1300 417 639</p>
          </div>
        </div>
      </div>
      <p class="contact__address">27C Marlow Parade, Ashvale VIC 3094, Australia</p>
    </div>
  </section>
</body>
</html>
```